Company Stationary, Business Card, Enevelopes, Letterhead
Would also like note stationary, and enevelope to fit
Company Stationary, Business Card, Enevelopes, Letterhead - Real Estate
Creative Brief
Professional
Dale Harwick
Designated Broker/Owner
2716 Juniper Loop Ste 214 Larkmoor Falls 99417
dale@brightfieldhomepartners.net
www.brightfieldhomepartners.net

```html
<!DOCTYPE html>
<html lang="en">
<head>
<meta charset="utf-8">
<title>Brightfield Home Partners — Business Card</title>
<link rel="stylesheet" href="https://fonts.googleapis.com/css2?family=Cinzel:wght@600&family=Cormorant+Garamond:wght@600&display=swap">
<style>
  :root {
    --page: #e9e9ea;
    --card: #ffffff;
    --red: #c8141c;
    --ink: #4a4a4a;
    --muted: #6d6d6d;
  }
  * { box-sizing: border-box; margin: 0; padding: 0; }
  html, body { width: 1200px; height: 980px; overflow: hidden; background: var(--page); }
  .sheet { position: relative; width: 1200px; height: 980px; }

  .card {
    position: absolute; left: 250px; width: 700px; height: 400px;
    background: var(--card); border-radius: 22px; overflow: hidden;
    box-shadow: 0 6px 18px rgba(0,0,0,0.12);
  }
  .card-back { top: 60px; }
  .card-front { top: 520px; }

  .brand-dot { border-radius: 50%; background: var(--red); flex: none; }
  .brand-name {
    font-family: "Cinzel", serif; font-weight: 600; color: var(--red);
    letter-spacing: 1px; white-space: nowrap;
  }

  /* back */
  .back-brand {
    position: absolute; top: 150px; left: 0; width: 100%;
    display: flex; align-items: center; justify-content: center; gap: 14px;
  }
  .back-brand .brand-dot { width: 30px; height: 30px; }
  .back-brand .brand-name { font-size: 34px; }
  .back-web {
    position: absolute; top: 222px; width: 100%; text-align: center;
    font-family: "Cormorant Garamond", serif; font-weight: 600;
    font-size: 15px; letter-spacing: 3px; color: var(--muted); text-transform: uppercase;
  }

  /* front */
  .front-brand {
    position: absolute; top: 44px; left: 40px;
    display: flex; align-items: center; gap: 12px;
  }
  .front-brand .brand-dot { width: 24px; height: 24px; }
  .front-brand .brand-name { font-size: 27px; }

  .contact-list {
    position: absolute; top: 118px; left: 40px; list-style: none;
    font-family: "Cormorant Garamond", serif; font-weight: 600;
    font-size: 15px; color: var(--ink); letter-spacing: 0.6px; line-height: 23px;
  }
  .contact-list li { display: flex; align-items: center; gap: 10px; white-space: nowrap; }
  .contact-icon { width: 14px; height: 14px; flex: none; }
  .contact-list .no-icon { padding-left: 24px; }

  .corner-band { position: absolute; inset: 0; width: 700px; height: 400px; }

  .person {
    position: absolute; left: 40px; top: 318px;
    font-family: "Cormorant Garamond", serif;
  }
  .person-name { font-family: "Cinzel", serif; font-weight: 600; font-size: 19px; color: var(--red); letter-spacing: 1px; }
  .person-title { font-weight: 600; font-size: 15px; color: var(--muted); letter-spacing: 1.5px; margin-top: 2px; }
</style>
</head>
<body>
<main class="sheet">

  <section class="card card-back" aria-label="Business card back">
    <div class="back-brand">
      <span class="brand-dot"></span>
      <span class="brand-name">BRIGHTFIELD</span>
    </div>
    <p class="back-web">www.brightfieldhomepartners.net</p>
  </section>

  <section class="card card-front" aria-label="Business card front">
    <svg class="corner-band" viewBox="0 0 700 400" aria-hidden="true">
      <path d="M700 230 Q640 350 560 400 L700 400 Z" fill="var(--red)"/>
    </svg>

    <div class="front-brand">
      <span class="brand-dot"></span>
      <span class="brand-name">BRIGHTFIELD</span>
    </div>

    <ul class="contact-list">
      <li>
        <svg class="contact-icon" viewBox="0 0 14 14"><circle cx="7" cy="7" r="7" fill="var(--red)"/><path d="M7 3a2.4 2.4 0 0 0-2.4 2.4C4.6 7.6 7 11 7 11s2.4-3.4 2.4-5.6A2.4 2.4 0 0 0 7 3z" fill="#fff"/></svg>
        2716 Juniper Loop Ste 214
      </li>
      <li class="no-icon">Larkmoor Falls, 99417</li>
      <li>
        <svg class="contact-icon" viewBox="0 0 14 14"><circle cx="7" cy="7" r="7" fill="var(--red)"/><path d="M4.5 3.5l1.6-.2.7 1.8-1 .8c.5 1 1.3 1.8 2.3 2.3l.8-1 1.8.7-.2 1.6C7 9.4 4.6 7 4.5 3.5z" fill="#fff"/></svg>
        555.010.0148
      </li>
      <li>
        <svg class="contact-icon" viewBox="0 0 14 14"><circle cx="7" cy="7" r="7" fill="var(--red)"/><rect x="4" y="5" width="6" height="4" fill="#fff"/></svg>
        555.010.0162
      </li>
      <li>
        <svg class="contact-icon" viewBox="0 0 14 14"><circle cx="7" cy="7" r="7" fill="var(--red)"/><rect x="3.5" y="4.5" width="7" height="5" fill="#fff"/><path d="M3.5 4.5L7 7.3l3.5-2.8" fill="none" stroke="var(--red)" stroke-width="0.8"/></svg>
        dale@brightfieldhomepartners.net
      </li>
      <li>
        <svg class="contact-icon" viewBox="0 0 14 14"><circle cx="7" cy="7" r="7" fill="var(--red)"/><circle cx="7" cy="7" r="3.4" fill="none" stroke="#fff" stroke-width="1"/><path d="M3.6 7h6.8" stroke="#fff" stroke-width="1"/></svg>
        www.brightfieldhomepartners.net
      </li>
    </ul>

    <div class="person">
      <p class="person-name">Dale Harwick</p>
      <p class="person-title">Designated Broker/Owner</p>
    </div>
  </section>

</main>
</body>
</html>
```